依頼詳細
ピロー包装の袋の掛ける短冊形のシールデザインを依頼させて頂きます。老舗感をパッケージから感じることができ、味噌まんじゅうの代替商品として品位とレトロ感を感じられるデザインを希望します。
記載項目
短冊
サイズ:W35mm×H270mm(詳細は添付資料参照)
印刷/カラー:グラビア印刷/

商品名「桜露ごよみ」
参考までに、容器の写真と、他社の短冊を掛けた商品イメージ写真を添付します。
希望イメージ
シンプル 複雑
単色 カラフル
暗い 明るい
日常 高級
遊び心 厳粛
未来的 伝統的
女性的 男性的
希望する色
色もお任せします
納品ファイル
• 高解像度JPG (.jpg)
• イラストレーター形式 (.ai)
補足説明
http://www.kiharado.co.jp/
弊社のサイトです。
■ 選んだ理由

当店のイメージと合いながらも他の商品との差別化がいいバランスで出来ているデザインでしたので、選定いたしました。

■ 提案者全員のお礼・コメント

何度も修正にお付き合い頂き誠にありがとうございます。

これからも素敵なデザインを産み出していって下さい。

```html
<!DOCTYPE html>
<html lang="ja">
<head>
<meta charset="utf-8">
<title>桜露ごよみ 短冊シール</title>
<link href="https://fonts.googleapis.com/css2?family=Yomogi&family=Noto+Sans+JP:wght@400&display=swap" rel="stylesheet">
<style>
  :root {
    --paper: #ffffff;
    --label-grey: #555555;
    --brown: #3b2314;
    --band-text: #e9d9b8;
    --orange: #ec8f4f;
    --amber: #f3b23d;
    --gold: #f6c55a;
    --green: #62a84a;
    --green-light: #8cc267;
    --cream: #fffdf1;
    --butter: #fbe9a6;
    --ink: #2a1a10;
  }
  html, body {
    margin: 0;
    width: 846px;
    height: 1200px;
    overflow: hidden;
    background: var(--paper);
  }
  .artboard {
    position: relative;
    width: 846px;
    height: 1200px;
  }
  .size-note {
    position: absolute;
    top: 24px;
    left: 246px;
    width: 250px;
    text-align: center;
    font: 15px "Noto Sans JP", sans-serif;
    color: var(--label-grey);
  }
  .tanzaku {
    position: absolute;
    top: 90px;
    left: 246px;
    width: 250px;
    height: 1086px;
    display: flex;
  }
  .edge-band {
    width: 34px;
    display: flex;
    flex-direction: column;
  }
  .edge-band .seg {
    flex: 1;
  }
  .edge-band .mark {
    background: var(--brown);
    color: var(--band-text);
    writing-mode: vertical-rl;
    font: 13px "Noto Sans JP", sans-serif;
    letter-spacing: 1px;
    display: flex;
    align-items: center;
    justify-content: center;
    flex: 1.3;
  }
  .edge-band.left .mark { transform: rotate(180deg); }
  .seg.orange { background: var(--orange); }
  .seg.amber { background: var(--amber); }
  .seg.gold { background: linear-gradient(var(--gold), var(--amber)); }
  .seg.green { background: var(--green); }
  .seg.green-light { background: linear-gradient(var(--green), var(--green-light)); }
  .center-panel {
    flex: 1;
    background:
      linear-gradient(90deg, var(--butter) 0%, var(--cream) 40%, var(--cream) 60%, var(--butter) 100%);
    position: relative;
    display: flex;
    justify-content: center;
    align-items: center;
  }
  .center-panel::before {
    content: "";
    position: absolute;
    inset: 0;
    background: linear-gradient(rgba(251,233,166,.6), rgba(255,253,241,0) 30%, rgba(255,253,241,0) 70%, rgba(251,233,166,.6));
  }
  .product-name {
    position: relative;
    writing-mode: vertical-rl;
    font: 58px/1 "Yomogi", cursive;
    color: var(--ink);
    letter-spacing: 2px;
    margin-top: -20px;
  }
</style>
</head>
<body>
<div class="artboard">
  <div class="size-note">w35mm×h270mm</div>
  <div class="tanzaku">
    <div class="edge-band left">
      <div class="seg mark">sakuragoyomi</div>
      <div class="seg orange"></div>
      <div class="seg mark">sakuragoyomi</div>
      <div class="seg amber"></div>
      <div class="seg mark">sakuragoyomi</div>
      <div class="seg gold"></div>
      <div class="seg mark">sakuragoyomi</div>
      <div class="seg amber"></div>
      <div class="seg mark">sakuragoyomi</div>
    </div>
    <div class="center-panel">
      <h1 class="product-name">桜露ごよみ</h1>
    </div>
    <div class="edge-band right">
      <div class="seg mark">sakuragoyomi</div>
      <div class="seg green"></div>
      <div class="seg mark">sakuragoyomi</div>
      <div class="seg mark">sakuragoyomi</div>
      <div class="seg green-light"></div>
      <div class="seg mark">sakuragoyomi</div>
      <div class="seg mark">sakuragoyomi</div>
      <div class="seg green"></div>
      <div class="seg mark">sakuragoyomi</div>
    </div>
  </div>
</div>
</body>
</html>
```